Tour Company Needs Poster for Box Office

We need a poster to promote walking tours in Aspen, Colorado. It should be attention grabbing with a vintage look similar to old west shows or circus promotions. It needs to promote "Birchvale Strolling Outings" 3 different tours (an evening ghost tour "Birchvale's NightVeil", a classic historic tour "Birchvale's Then and Now" & a sightseeing tour "Beyond the Quiet Lane"). Attached images should be used in conjunction with the different tour promotions. Poster should be full color and the size needs to be 24" wide X 36 " high.

Requirements
Must have
• Individual tour tag lines
Birchvale's NightVeil "Ghosts Murder & Mayhem"
Birchvale's Then and Now" Classic Historical Tour"
Beyond the Quiet Lane "Historic West End to the River"

Company Logo can be small towards the bottom of the poster and paired with the quote "Like Pellow he Loves Spinning Tales! -Kelbrook's Journeys"

website should be included www.BirchvaleStrollingOutings.example
Nice to have
• Small Quotes to include
"theatrics, humor, wit and dazzling manner"
"awesome story teller"
"should not be missed"

```html
<!DOCTYPE html>
<html lang="en">
<head>
<meta charset="utf-8">
<title>Birchvale Strolling Outings – Tour Poster</title>
<link rel="stylesheet" href="https://fonts.googleapis.com/css2?family=Lato:wght@300;400&family=Josefin+Sans:wght@400&family=Pathway+Gothic+One&display=swap">
<style>
  :root {
    --paper: #fbfbfb;
    --paper-shade: #ececec;
    --stone: #8f8c89;
    --stone-dark: #7d7a77;
    --mauve: #9a8d93;
    --sky-line: #b9dcef;
    --forest: #2f4a3d;
    --ink: #1e1e1e;
    --quote-ink: #3a4440;
    --brand-red: #a51d1d;
    --white: #ffffff;
  }
  html, body {
    margin: 0;
    padding: 0;
    width: 872px;
    height: 1200px;
    overflow: hidden;
    background: var(--paper);
  }
  .poster { display: block; width: 872px; height: 1200px; }
  .tour-title { font-family: "Lato", sans-serif; font-weight: 400; fill: var(--white); }
  .tour-title--alt { font-family: "Josefin Sans", sans-serif; }
  .tour-tagline { font-family: "Lato", sans-serif; fill: var(--white); }
  .tour-tagline--alt { font-family: "Josefin Sans", sans-serif; }
  .press-quote { font-family: "Pathway Gothic One", sans-serif; fill: var(--ink); }
  .review-quote { font-family: "Pathway Gothic One", sans-serif; fill: var(--quote-ink); }
  .brand-name { font-family: "Pathway Gothic One", sans-serif; fill: var(--brand-red); }
  .website { font-family: "Pathway Gothic One", sans-serif; fill: var(--ink); }
</style>
</head>
<body>
<svg class="poster" viewBox="0 0 872 1200" xmlns="http://www.w3.org/2000/svg">
  <defs>
    <linearGradient id="night-tones" x1="0" y1="0" x2="1" y2="1">
      <stop offset="0" stop-color="#b9b6b2"/>
      <stop offset="0.5" stop-color="#6f6c69"/>
      <stop offset="1" stop-color="#2c2a29"/>
    </linearGradient>
    <linearGradient id="valley-tones" x1="0" y1="0" x2="0" y2="1">
      <stop offset="0" stop-color="#cfd9d8"/>
      <stop offset="0.25" stop-color="#6f8a4f"/>
      <stop offset="0.7" stop-color="#4f6b34"/>
      <stop offset="1" stop-color="#9c9787"/>
    </linearGradient>
    <linearGradient id="trail-tones" x1="0" y1="0" x2="1" y2="1">
      <stop offset="0" stop-color="#3f5a2e"/>
      <stop offset="0.5" stop-color="#6a8246"/>
      <stop offset="1" stop-color="#2d3f22"/>
    </linearGradient>
    <linearGradient id="paper-fade" x1="0" y1="0" x2="1" y2="0">
      <stop offset="0" stop-color="var(--paper)"/>
      <stop offset="1" stop-color="var(--paper-shade)"/>
    </linearGradient>
    <filter id="soft-shadow" x="-10%" y="-30%" width="120%" height="160%">
      <feDropShadow dx="2" dy="3" stdDeviation="2" flood-color="#000" flood-opacity="0.35"/>
    </filter>
  </defs>

  <rect class="poster-paper" x="0" y="0" width="872" height="1200" fill="url(#paper-fade)"/>

  <!-- NightVeil tour -->
  <g class="tour tour--nightveil">
    <polygon points="23,23 847,23 847,392 23,352" fill="var(--stone)"/>
    <polygon points="508,23 847,23 847,392 590,383" fill="url(#night-tones)"
             role="img" aria-label="Photo of costumed guides in period dress holding a lantern"/>
    <text class="tour-title" x="40" y="196" font-size="56">Birchvale's NightVeil</text>
    <text class="tour-tagline" x="92" y="239" font-size="24">"Ghosts Murder &amp; Mayhem"</text>
  </g>

  <line x1="23" y1="354" x2="847" y2="366" stroke="var(--sky-line)" stroke-width="3"/>

  <!-- Then and Now tour -->
  <g class="tour tour--then-and-now">
    <polygon points="23,358 847,370 847,690 23,697" fill="#d9d7d6"/>
    <polygon points="23,360 480,366 455,697 23,697" fill="url(#valley-tones)"
             role="img" aria-label="Photo of the guide in a hat and vest standing before a green mountain valley"/>
    <polygon points="470,380 847,380 847,673 446,673" fill="var(--mauve)"/>
    <text class="tour-title tour-title--alt" x="650" y="482" font-size="40" text-anchor="middle">Birchvale's</text>
    <text class="tour-title tour-title--alt" x="650" y="519" font-size="40" text-anchor="middle">Then and Now</text>
    <text class="tour-tagline tour-tagline--alt" x="650" y="572" font-size="25" text-anchor="middle">"Classic Historical Tour"</text>
  </g>

  <!-- Quiet Lane tour -->
  <g class="tour tour--quiet-lane">
    <polygon points="23,697 440,688 440,955 23,955" fill="var(--forest)"/>
    <polygon points="429,688 847,680 847,965 429,955" fill="url(#trail-tones)"
             role="img" aria-label="Photo of wooden trail signposts among leafy trees"/>
    <text class="tour-title tour-title--alt" x="226" y="754" font-size="40" text-anchor="middle">Beyond the Quiet</text>
    <text class="tour-title tour-title--alt" x="226" y="792" font-size="40" text-anchor="middle">Lane</text>
    <text class="tour-tagline tour-tagline--alt" x="62" y="850" font-size="25">"Historic West End</text>
    <text class="tour-tagline tour-tagline--alt" x="62" y="887" font-size="25">to the River"</text>
  </g>

  <!-- Footer: press quote, brand, reviews, website -->
  <g class="footer">
    <text class="press-quote" x="165" y="980" font-size="28" text-anchor="middle">"Like Pellow he Loves</text>
    <text class="press-quote" x="170" y="1024" font-size="28" text-anchor="middle">Spinning Tales! -Kelbrook's Journeys"</text>

    <text class="brand-name" x="170" y="1080" font-size="30" text-anchor="middle">Birchvale Strolling</text>
    <text class="brand-name" x="170" y="1114" font-size="30" text-anchor="middle">Outings</text>

    <text class="review-quote" x="356" y="1018" font-size="44" filter="url(#soft-shadow)">"awesome story teller"</text>
    <text class="review-quote" x="836" y="1088" font-size="44" text-anchor="end" filter="url(#soft-shadow)">"should not be missed"</text>
    <text class="website" x="836" y="1162" font-size="36" text-anchor="end">www.BirchvaleStrollingOutings.example</text>
  </g>
</svg>
</body>
</html>
```